TRVL-NINE Web Design

We are a Health, Safety, Environmental & Quality Recruitment Agency, our clients are major corporate Mining, Oil & Gas and Engineering companies. We have offices in Perth & Melbourne, Australia

The website should be very functional & easy to navigate

BUT REALLY LOOKING FOR WOW FACTOR!

Please Note: TRVL CORPORATE IS OUR OLD COMPANY THE NEW ONE IS "TRVL-NINE" 

Some idea's from our competitors:

http://www.guardlinepeak.com.au/
http://www.vantagehiring.com.au/
http://www.brightpick.com.au/
http://www.kovastaffing.co.uk/
http://www.jobmarrow.com/health-safety-environment-jobs

Would love to see some of our valued clients and there logos

still looking for wow factor

Industry/Entity Type

Mining

Requirements
Must have
• A place where candidates can upload there resumes & other contact details
• eg: http://www.guardlinepeak.com.au/candidates/register-your-resume/
• A place we can load jobs on to eg: http://www.guardlinepeak.com.au/vacancies/
• Contact details:
• Perth: 12 Kestrel Ave, West Perth, Western Australia 6005
• t: 08 7153 4406 | f: 08 7153 4470 |
• Melbourne: Level 1, 218 Arbour Lane, Melbourne, Victoria 3000
• t: 03 6214 5072| f: 03 6231 4095 |
• e: dennisk@trvlnine.com.au | w: http://www.trvlnine.com.au

```html
<!DOCTYPE html>
<html lang="en">
<head>
<meta charset="utf-8">
<title>Trvlnine – HSEQ Recruitment</title>
<link rel="stylesheet" href="https://fonts.googleapis.com/css2?family=Arvo&family=Raleway:wght@500;600&family=Arimo:wght@400;700&display=swap">
<style>
:root{
  --cyan:#1aa6c9;
  --cyan-dark:#1488a8;
  --ink:#1b1b1b;
  --text:#2a2a2a;
  --nav:#232323;
  --paper:#f4f4f4;
  --paper-grey:#ebebeb;
  --footer:#3b3b3b;
  --footer-text:#e6e6e6;
  --white:#ffffff;
  --field:#e9e9e9;
  --field-line:#c9c9c9;
}
*{box-sizing:border-box;margin:0;padding:0}
html,body{width:847px;height:1200px;overflow:hidden}
body{position:relative;background:var(--paper);font-family:"Arimo",Arial,sans-serif;color:var(--text)}
.abs{position:absolute}

.site-header{left:0;top:0;width:847px;height:108px;background:linear-gradient(#f2f2f2,#e4e4e4)}
.brand{left:0;width:847px;top:30px;text-align:center;font-family:"Raleway",sans-serif;font-weight:500;font-size:34px;letter-spacing:1px;color:var(--cyan-dark)}
.brand-mark{display:inline-block;width:44px;height:44px;background:#6c7b86;vertical-align:middle;margin-right:12px}

.main-nav{left:0;top:108px;width:847px;height:33px;background:var(--nav);border-bottom:3px solid #111}
.nav-item{top:8px;font-family:"Raleway",sans-serif;font-weight:600;font-size:9.5px;color:var(--white);letter-spacing:.2px}
.nav-item.active{top:8px;left:78px;width:53px;height:19px;background:var(--cyan);border-radius:2px;text-align:center;line-height:19px;top:7px}
.nav-phone{left:644px;top:7px;color:var(--white);font-family:"Raleway",sans-serif;font-size:13px;display:flex;align-items:center;gap:6px}

.hero-band{left:0;top:141px;width:847px;height:375px;background:var(--cyan)}
.hero-frame{left:83px;top:33px;width:687px;height:282px;background:var(--white);border-radius:3px;box-shadow:0 2px 6px rgba(0,0,0,.25)}
.hero-photo{left:7px;top:7px;width:673px;height:266px;background:linear-gradient(100deg,#2a3c6a 0%,#5a6f8d 35%,#b9c6d3 60%,#dfe6ee 100%)}
.social-title{left:85px;top:330px;font-family:"Arvo",serif;font-size:14px;color:var(--ink)}
.social-sub{left:85px;top:349px;font-family:"Arvo",serif;font-size:9px;color:var(--white)}
.social-dot{top:328px;width:31px;height:31px;border-radius:50%;background:var(--white);border:3px solid #3a6fb8}
.email-line{left:513px;top:337px;font-family:"Arvo",serif;font-size:14px;color:var(--ink)}
.email-line span{color:var(--white);margin-left:6px}

.lower-grey{left:0;top:690px;width:847px;height:365px;background:var(--paper-grey)}

.card{top:559px;width:199px;height:160px;background:var(--white);border:1px solid #e0e0e0;border-radius:4px;box-shadow:0 1px 3px rgba(0,0,0,.08);text-align:center}
.card-img{position:absolute;left:13px;top:12px;width:170px;height:71px}
.card-title{position:absolute;left:0;width:100%;top:90px;font-family:"Raleway",sans-serif;font-weight:500;font-size:16px;color:var(--cyan-dark)}
.card-text{position:absolute;left:8px;right:8px;top:110px;font-size:8.4px;line-height:12.8px;color:var(--text)}
.card-tab{position:absolute;left:72px;bottom:-18px;width:56px;height:20px;background:var(--white);border-radius:0 0 28px 28px}
.card-tab::after{content:"";position:absolute;left:20px;top:2px;border-left:8px solid transparent;border-right:8px solid transparent;border-top:8px solid #222}

.why-title{left:76px;top:767px;font-family:"Arvo",serif;font-size:22px;color:var(--cyan-dark)}
.why-rule{left:77px;top:799px;width:456px;height:1px;background:#cfcfcf}
.why-text{left:77px;top:807px;width:465px;font-size:9.4px;line-height:14px;color:var(--ink)}
.why-text p{margin-bottom:14px}

.enquiry{left:553px;top:752px;width:211px;height:268px;background:#f1f1f1;border:1px solid #e2e2e2;border-radius:3px}
.enquiry-head{left:5px;top:10px;width:199px;height:26px;background:linear-gradient(#444,#111);border-radius:3px;color:var(--white);font-family:"Arvo",serif;font-size:15px;padding:3px 9px}
.field{left:6px;width:197px;background:var(--field);border:1px solid var(--field-line);border-radius:3px;box-shadow:inset 0 2px 2px rgba(0,0,0,.12);font-size:8.6px;color:#333;padding:9px 9px}
.submit{left:139px;top:236px;width:65px;height:19px;background:linear-gradient(#555,#111);border-radius:4px;color:var(--white);font-size:9px;font-weight:700;text-align:center;line-height:19px}

.site-footer{left:0;top:1055px;width:847px;height:145px;background:var(--footer)}
.foot-col{top:22px;color:var(--footer-text)}
.foot-col h4{font-family:"Raleway",sans-serif;font-weight:600;font-size:13px;color:var(--white);margin-bottom:8px}
.foot-col li{list-style:none;font-size:8.6px;line-height:16.5px;padding-left:1px}
.foot-brand{left:570px;top:22px;width:157px;font-family:"Raleway",sans-serif;font-weight:500;font-size:22px;color:#d4d4d4;display:flex;align-items:center;gap:8px}
.foot-brand i{display:inline-block;width:36px;height:36px;background:#777}
.foot-copy{left:540px;top:73px;width:220px;text-align:center;font-size:9.4px;line-height:17px;color:var(--footer-text)}
.foot-social{top:112px;width:19px;height:19px;border-radius:50%;background:var(--white)}
</style>
</head>
<body>

<header class="site-header abs">
  <div class="brand abs"><span class="brand-mark"></span>trvlnine</div>
</header>

<nav class="main-nav abs">
  <div class="nav-item active abs">HOME</div>
  <div class="nav-item abs" style="left:160px">ABOUT US</div>
  <div class="nav-item abs" style="left:251px">EMPLOYERS</div>
  <div class="nav-item abs" style="left:350px">CANDIDATES</div>
  <div class="nav-item abs" style="left:455px">VACANCIES</div>
  <div class="nav-item abs" style="left:551px">CONTACT</div>
  <div class="nav-phone abs">
    <svg width="10" height="15" viewBox="0 0 10 15"><rect x="1" y="0.5" width="8" height="14" rx="1" fill="none" stroke="#fff"/><rect x="2.5" y="2" width="5" height="4" fill="#fff"/><g fill="#fff"><rect x="2.5" y="7.5" width="1.5" height="1.5"/><rect x="6" y="7.5" width="1.5" height="1.5"/><rect x="2.5" y="10" width="1.5" height="1.5"/><rect x="6" y="10" width="1.5" height="1.5"/></g></svg>
    123 456 7890
  </div>
</nav>

<section class="hero-band abs">
  <div class="hero-frame abs">
    <div class="hero-photo abs" role="img" aria-label="Worker in hard hat on a phone in front of an oil refinery"></div>
  </div>
  <div class="social-title abs">Find Us On Social Network:</div>
  <div class="social-sub abs">Bayarsety kertya aset aplicaboes kerasaer</div>
  <div class="social-dot abs" style="left:309px"></div>
  <div class="social-dot abs" style="left:353px"></div>
  <div class="email-line abs">Email:<span>perth@trvlnine.com.au</span></div>
</section>

<div class="lower-grey abs"></div>

<article class="card abs" style="left:87px">
  <div class="card-img" role="img" aria-label="Offshore oil platform" style="background:linear-gradient(#dfe3e6 0%,#b7b9ae 45%,#d6b82a 75%,#8e97a0 100%)"></div>
  <div class="card-title">CANDIDATES</div>
  <div class="card-text">Vestibulum rutrum pharetra diam, eget dapi-bus leo vehicula ut. Fusce aliquam, odio eget adipiscing lobortis.</div>
  <div class="card-tab"></div>
</article>
<article class="card abs" style="left:324px">
  <div class="card-img" role="img" aria-label="Two engineers in hard hats" style="top:17px;background:linear-gradient(90deg,#c9872f 0%,#9fb6cd 45%,#2f4f87 100%)"></div>
  <div class="card-title" style="top:95px">QAQC ENGINEERS</div>
  <div class="card-text" style="top:115px">Vestibulum rutrum pharetra diam, eget dapi-bus leo vehicula ut. Fusce aliquam, odio eget adipiscing lobortis.</div>
  <div class="card-tab"></div>
</article>
<article class="card abs" style="left:564px">
  <div class="card-img" role="img" aria-label="Offshore supply vessel at sea" style="top:17px;background:linear-gradient(#9ec3e6 0%,#5a7fb8 45%,#1d3d8c 80%,#2b4d7a 100%)"></div>
  <div class="card-title" style="top:95px">VACANCIES</div>
  <div class="card-text" style="top:115px">Vestibulum rutrum pharetra diam, eget dapi-bus leo vehicula ut. Fusce aliquam, odio eget adipiscing lobortis.</div>
  <div class="card-tab"></div>
</article>

<h2 class="why-title abs">Why work with Trvlnine?</h2>
<div class="why-rule abs"></div>
<div class="why-text abs">
  <p>Working from the largestdatabase of industry professionalsin Australia, TRVL-NINE operates exclusively in the Mining, Oil &amp; Gas, Construction and Engineering sectors. Our clients range from engineering consultan-cies and major owner-operator oil companies to international EPCM’s and the largest diversified mining companies in the world.</p>
  <p>In addition to providing Health, Safety, Environment and Quality professionals, we also deliver highly quali-fied and experienced Risk Management, Emergency Response and Training personnel at all levels.</p>
  <p>Today’s dynamic and ever-changing workplaces require recruiters to up the ante – that’s where we come in. With offices in Perth, Brisbane,Seoul and Hong Kong, we source both locally and internationally to meet the unique requirements of our clients and candidates. Our passion for the industry and commitment to ensuring a safer work environment for all is the foundation of everything we do.</p>
</div>

<aside class="enquiry abs">
  <div class="enquiry-head abs">Quick Enquiry</div>
  <div class="field abs" style="top:56px;height:25px">Your Name</div>
  <div class="field abs" style="top:92px;height:25px">Email Address</div>
  <div class="field abs" style="top:129px;height:25px">Phone</div>
  <div class="field abs" style="top:166px;height:60px">Your Comments</div>
  <div class="submit abs">Submit Now</div>
</aside>

<footer class="site-footer abs">
  <div class="foot-col abs" style="left:79px">
    <h4>WHO WE ARE</h4>
    <ul><li>Company</li><li>News</li><li>Team</li><li>Careers</li><li>Contact</li></ul>
  </div>
  <div class="foot-col abs" style="left:210px">
    <h4>WHAT WE DO</h4>
    <ul><li>What is Trvlnine ?</li><li>Live Demo</li><li>Resources</li><li>FAQs</li><li>Mobile Apps</li></ul>
  </div>
  <div class="foot-col abs" style="left:359px">
    <h4>WHO WE WORK WITH</h4>
    <ul><li>Utilities</li><li>Consumers</li><li>Partners</li><li>Get Started</li></ul>
  </div>
  <div class="foot-brand abs"><i></i>trvlnine</div>
  <div class="foot-copy abs">2006 - 2013 &nbsp;Trvlnine &nbsp;Privacy Policy Terms of Conditions. All Rights Reserved</div>
  <div class="foot-social abs" style="left:588px"></div>
  <div class="foot-social abs" style="left:613px"></div>
  <div class="foot-social abs" style="left:639px"></div>
  <div class="foot-social abs" style="left:665px"></div>
  <div class="foot-social abs" style="left:690px"></div>
</footer>

</body>
</html>
```